2 x storefront vinyl request

We are transitioning to a storefront office and need two vinyls for the windows.

First vinyl: Use the Halloway Partners logo, website (www.hallowaypartnersestates.example) and leasing office number ((555) 314-2786)

Second vinyl: Maintenance Division & phone number (555) 314-2786

```html
<!DOCTYPE html>
<html lang="en">
<head>
<meta charset="utf-8">
<title>Halloway Partners – Storefront Vinyls</title>
<link rel="stylesheet" href="https://fonts.googleapis.com/css2?family=Open+Sans:wght@700;800&family=Noto+Serif:wght@500&display=swap">
<style>
  :root {
    --page: #ffffff;
    --vinyl-white: #ffffff;
    --ink: #161616;
    --band-grey: #a3a3a3;
    --accent-green: #7dc242;
    --shadow: rgba(0, 0, 0, 0.45);
  }
  * { margin: 0; padding: 0; box-sizing: border-box; }
  html, body {
    width: 1200px;
    height: 885px;
    overflow: hidden;
    background: var(--page);
  }
  .canvas {
    position: relative;
    width: 1200px;
    height: 885px;
  }
  .vinyl {
    position: absolute;
    left: 108px;
    width: 983px;
    height: 318px;
    background: var(--vinyl-white);
    box-shadow: 0 0 38px var(--shadow);
    overflow: hidden;
  }
  .vinyl--leasing { top: 78px; }
  .vinyl--maintenance { top: 468px; }

  .vinyl__grey-rule {
    position: absolute;
    left: 0;
    width: 100%;
    height: 15px;
    background: var(--band-grey);
  }
  .vinyl__black-band {
    position: absolute;
    left: 0;
    width: 100%;
    bottom: 0;
    background: var(--ink);
    display: flex;
    align-items: center;
    justify-content: center;
  }

  /* Leasing vinyl */
  .vinyl--leasing .vinyl__grey-rule { top: 233px; }
  .vinyl--leasing .vinyl__black-band { top: 248px; }

  .brand-name {
    position: absolute;
    left: 24px;
    top: 118px;
    width: 220px;
    display: flex;
    align-items: center;
    gap: 10px;
    font-family: "Open Sans", sans-serif;
    font-weight: 800;
    font-size: 25px;
    line-height: 1.05;
    color: var(--ink);
    text-transform: uppercase;
  }
  .brand-name__square {
    flex: none;
    width: 22px;
    height: 22px;
    background: var(--ink);
  }

  .phone-icon {
    fill: var(--accent-green);
    display: block;
  }
  .leasing-phone__icon {
    position: absolute;
    left: 254px;
    top: 71px;
  }
  .phone-number {
    font-family: "Noto Serif", serif;
    font-weight: 500;
    color: var(--accent-green);
    white-space: nowrap;
  }
  .leasing-phone__number {
    position: absolute;
    left: 360px;
    top: 82px;
    font-size: 92px;
    line-height: 1;
    letter-spacing: -4px;
  }
  .website {
    font-family: "Open Sans", sans-serif;
    font-weight: 700;
    font-size: 41px;
    color: var(--vinyl-white);
    letter-spacing: 0.5px;
    text-transform: uppercase;
  }

  /* Maintenance vinyl */
  .vinyl--maintenance .vinyl__grey-rule { top: 156px; }
  .vinyl--maintenance .vinyl__black-band { top: 171px; gap: 14px; }

  .division-title {
    position: absolute;
    left: 0;
    top: 0;
    width: 100%;
    height: 156px;
    display: flex;
    align-items: center;
    justify-content: center;
    font-family: "Open Sans", sans-serif;
    font-weight: 800;
    font-size: 74px;
    color: var(--ink);
    letter-spacing: 0;
  }
  .maintenance-phone__number {
    font-size: 112px;
    line-height: 1;
    letter-spacing: -5px;
    margin-top: -6px;
  }
</style>
</head>
<body>
<main class="canvas">

  <section class="vinyl vinyl--leasing" aria-label="Leasing office vinyl">
    <div class="brand-name">
      <span class="brand-name__square" aria-hidden="true"></span>
      <span>Halloway Partners</span>
    </div>

    <svg class="phone-icon leasing-phone__icon" width="102" height="130" viewBox="2 2 20 20" preserveAspectRatio="none" aria-hidden="true">
      <path d="M6.62 10.79c1.44 2.83 3.76 5.14 6.59 6.59l2.2-2.2c.27-.27.67-.36 1.02-.24 1.12.37 2.33.57 3.57.57.55 0 1 .45 1 1V20c0 .55-.45 1-1 1-9.39 0-17-7.61-17-17 0-.55.45-1 1-1h3.5c.55 0 1 .45 1 1 0 1.25.2 2.45.57 3.57.11.35.03.74-.25 1.02l-2.2 2.2z"/>
    </svg>
    <p class="phone-number leasing-phone__number">(555) 314-2786</p>

    <div class="vinyl__grey-rule"></div>
    <div class="vinyl__black-band">
      <p class="website">hallowaypartnersestates.example</p>
    </div>
  </section>

  <section class="vinyl vinyl--maintenance" aria-label="Maintenance division vinyl">
    <h2 class="division-title">MAINTENANCE DIVISION</h2>
    <div class="vinyl__grey-rule"></div>
    <div class="vinyl__black-band">
      <svg class="phone-icon" width="90" height="114" viewBox="2 2 20 20" preserveAspectRatio="none" aria-hidden="true">
        <path d="M6.62 10.79c1.44 2.83 3.76 5.14 6.59 6.59l2.2-2.2c.27-.27.67-.36 1.02-.24 1.12.37 2.33.57 3.57.57.55 0 1 .45 1 1V20c0 .55-.45 1-1 1-9.39 0-17-7.61-17-17 0-.55.45-1 1-1h3.5c.55 0 1 .45 1 1 0 1.25.2 2.45.57 3.57.11.35.03.74-.25 1.02l-2.2 2.2z"/>
      </svg>
      <p class="phone-number maintenance-phone__number">(555) 314-2786</p>
    </div>
  </section>

</main>
</body>
</html>
```